Redesign our iOS App Design mockups

- Redesign our current Zelvo App Mockup
- Keep the design simple so that programmers do not have to do too much extra work to make your design work.
- Look at the attached website screenshot for the overall look and feel, and color scheme
- Convert the attached vector logo to iOS Icon format.
- Deliver all graphics in the density required for Zelvo QT Grand.
- I have attached the current iOS mockup in a .ZIP file but you can view it here as well: https://boards.kelmoraview.com/share/TRWQBN8HDK2

Target Market(s)

Mostly Male Internet Consumers between the ages of 20 and 35

Industry/Entity Type

Internet

Colors

Designer to choose colors to be used in the design.

Requirements
Must have
• - Deliver all graphics in the density required for Zelvo QT Grand
• - Should also look good on Murel and Murel pro
• - Design type should be “FLAT.”
• - Spell out fonts used in the design and where they are used. Also, include font sizes.
• - Please use ALL the elements in each page and use all placements and text EXACTLY. Please do not improvise with text or components.
• I have designed the mockup exactly the way I like it. I just want it to made to look better.
Should not have

```html
<!DOCTYPE html>
<html lang="en">
<head>
<meta charset="utf-8">
<title>NestVPN — iOS App Screens</title>
<link href="https://fonts.googleapis.com/css2?family=Nunito+Sans:wght@300;400;600;700;800&display=swap" rel="stylesheet">
<style>
:root{
  --canvas:#e0e0e0;
  --screen:#ffffff;
  --bar:#f7f7f7;
  --ink:#1c1c1c;
  --muted:#6b6b6b;
  --line:#e3e3e3;
  --brand:#f4584a;
  --brand-light:#ff7c5e;
  --blue-a:#00c8ff;
  --blue-b:#0a8cff;
  --band:#141414;
  --dim:#8c8c8c;
  --toggle:#4cbb5c;
  --star:#555555;
  --star-gold:#f7d21b;
}
*{box-sizing:border-box;margin:0;padding:0}
html,body{width:1200px;height:1200px;overflow:hidden;background:var(--canvas)}
body{font-family:"Nunito Sans",Helvetica,sans-serif;color:var(--ink)}
.board{position:absolute;left:0;top:0;width:1500px;height:1500px;transform:scale(.8);transform-origin:0 0}
.screen{position:absolute;width:300px;height:648px;background:var(--screen);overflow:hidden}
.screen>*{position:absolute}
.status{left:0;top:0;width:100%;height:70px;background:var(--bar);border-bottom:1px solid var(--line)}
.status .time{position:absolute;left:26px;top:11px;font-size:12px;font-weight:700}
.status .icons{position:absolute;right:12px;top:13px}
.home-bar{left:96px;bottom:8px;width:107px;height:3px;border-radius:2px;background:var(--ink)}
.brand-mark{display:flex;flex-direction:column;align-items:center;left:0;width:100%}
.brand-dot{width:84px;height:84px;border-radius:50%;background:var(--brand)}
.brand-name{margin-top:26px;font-size:25px;font-weight:800;letter-spacing:-.5px;color:var(--ink)}
.loading{left:0;width:100%;top:382px;text-align:center;font-size:16px;font-weight:700}
.spinner{left:136px;top:418px}
.label{font-size:13px;color:var(--muted)}
.field{width:202px;height:26px;border:1px solid var(--line);border-radius:7px;font-size:11px;padding:5px 10px;display:flex;justify-content:space-between;align-items:center}
.field .clear{width:10px;height:10px;border-radius:50%;background:#d4d4d4}
.caret{display:inline-block;width:1px;height:11px;background:var(--brand);vertical-align:middle}
.pill-btn{border-radius:22px;background:linear-gradient(90deg,var(--brand-light),var(--brand));color:#fff;text-align:center;box-shadow:0 5px 10px rgba(244,88,74,.3)}
.small-note{font-size:8px;color:var(--muted)}
.signup{left:0;width:100%;top:595px;text-align:center;font-size:9px;color:var(--muted)}
.signup b{color:var(--brand)}
.topnav{left:0;top:38px;width:100%;height:32px}
.hamburger{position:absolute;left:20px;top:9px;width:20px;height:12px;border-top:2px solid var(--ink);border-bottom:2px solid var(--ink)}
.hamburger::after{content:"";position:absolute;left:0;top:3px;width:20px;height:2px;background:var(--ink)}
.nav-title{position:absolute;left:0;width:100%;top:6px;text-align:center;font-size:13px;font-weight:700}
.ping{position:absolute;right:15px;top:-2px;text-align:center;font-size:7px;color:var(--muted)}
.ping i{display:block;width:10px;height:10px;margin:0 auto 1px;border:1px solid var(--blue-b);border-radius:50%}
.status-band{left:0;top:71px;width:100%;height:34px;background:var(--band);color:var(--brand);font-size:14px;font-weight:600;text-align:center;line-height:34px}
.quick{left:60px;top:116px;width:180px;height:30px;border-radius:15px;background:linear-gradient(90deg,var(--blue-a),var(--blue-b));color:#fff;font-size:14px;font-weight:600;text-align:center;line-height:30px;box-shadow:0 4px 10px rgba(10,140,255,.3)}
.section{left:20px;font-size:12px;color:var(--muted)}
.card{left:16px;width:266px;height:36px;border-radius:18px;background:#fff;box-shadow:0 2px 5px rgba(0,0,0,.16);display:flex;align-items:center;padding:0 14px 0 16px;font-size:15px}
.card.country{padding-left:12px;font-weight:700}
.card .grow{flex:1}
.flag{width:25px;height:25px;border-radius:50%;margin-right:9px}
.flag.de{background:linear-gradient(#1a1a1a 0 33%,#dd0000 33% 66%,#ffce00 66%)}
.flag.us{background:linear-gradient(90deg,#27367a 0 45%,transparent 45%),repeating-linear-gradient(#d22 0 3px,#fff 3px 6px)}
.flag.uk{background:radial-gradient(circle,#cc1126 0 25%,#ffffff 25% 35%,#1f3a8a 35%)}
.flag.ca{background:linear-gradient(90deg,#d52b1e 0 28%,#fff 28% 72%,#d52b1e 72%)}
.flag.in{background:linear-gradient(#ff9933 0 33%,#fff 33% 66%,#138808 66%)}
.star{color:var(--star);font-size:14px;margin-right:12px}
.star.gold{color:var(--star-gold)}
.chev{width:8px;height:8px;border-right:2px solid var(--ink);border-top:2px solid var(--ink);transform:rotate(45deg)}
.menu-head{left:0;top:0;width:219px;height:141px;background:var(--brand)}
.menu-head .time{position:absolute;left:26px;top:11px;font-size:12px;font-weight:700;color:var(--ink)}
.menu-logo{position:absolute;left:22px;top:40px;display:flex;align-items:center}
.menu-logo span{width:56px;height:56px;border-radius:50%;background:#fff;margin-right:12px}
.menu-logo b{font-size:23px;font-weight:800;color:#fff;letter-spacing:-.5px}
.menu-shade{left:219px;top:0;width:82px;height:650px;background:var(--dim)}
.menu-shade .icons{position:absolute;right:12px;top:13px}
.menu-shade .ping{right:15px;top:36px;color:#333}
.shade-band{position:absolute;left:0;top:71px;width:100%;height:34px;background:var(--band)}
.shade-blue{position:absolute;left:-12px;top:117px;width:32px;height:30px;border-radius:15px;background:var(--blue-b)}
.stub{position:absolute;left:-20px;width:84px;height:36px;border-radius:18px;background:#8c8c8c;box-shadow:0 2px 5px rgba(0,0,0,.3);display:flex;align-items:center;justify-content:flex-end;padding-right:22px}
.stub .chev{border-color:#222}
.stub .star{color:#333;font-size:13px;margin-right:10px}
.stub .star.gold{color:#b9a23a}
.menu-item{left:0;width:219px;height:37px;padding-left:30px;font-size:16px;color:#333;line-height:37px}
.menu-item.active{background:#efefef;color:var(--brand);font-weight:700}
.back{position:absolute;left:20px;top:9px;font-size:12px;color:var(--brand)}
.page-title{position:absolute;top:8px;font-size:13px;font-weight:700}
.group-title{left:26px;top:104px;font-size:17px;color:#555;font-weight:300}
.list{left:0;top:135px;width:100%;border-top:1px solid var(--line);border-bottom:1px solid var(--line)}
.row{position:relative;height:50px;padding:6px 28px;border-bottom:1px solid var(--line)}
.row:last-child{border-bottom:none}
.row h3{font-size:15px;font-weight:400}
.row p{font-size:12px;color:#555;font-weight:300;line-height:1.2}
.tick{position:absolute;right:18px;top:16px}
.row.switch{height:66px}
.toggle{position:absolute;right:18px;top:19px;width:40px;height:24px;border-radius:12px;background:var(--toggle)}
.toggle::after{content:"";position:absolute;right:2px;top:2px;width:20px;height:20px;border-radius:50%;background:#fff}
.row.link{height:38px;display:flex;align-items:center;font-size:15px;padding-left:28px}
.row.link svg{margin-right:12px}
.row.link.danger{color:var(--brand)}
.footer-links{left:24px;font-size:12px}
.forgot-head{left:28px;top:105px;font-size:17px}
.forgot-copy{left:28px;top:130px;width:252px;font-size:9px;line-height:1.25;color:#555}
.submit{left:28px;top:255px;width:202px;height:24px;font-size:11px;line-height:24px}
</style>
</head>
<body>
<div class="board">

  <!-- Splash -->
  <section class="screen" style="left:67px;top:76px;height:646px">
    <header class="status"><span class="time">9:41</span>
      <svg class="icons" width="54" height="10" viewBox="0 0 54 10"><rect x="0" y="6" width="2" height="4" fill="#1c1c1c"/><rect x="3" y="4" width="2" height="6" fill="#1c1c1c"/><rect x="6" y="2" width="2" height="8" fill="#1c1c1c"/><rect x="9" y="0" width="2" height="10" fill="#1c1c1c"/><path d="M16 4a8 8 0 0 1 11 0M18 6a5 5 0 0 1 7 0" stroke="#1c1c1c" stroke-width="1.6" fill="none"/><circle cx="21.5" cy="8.5" r="1.3" fill="#1c1c1c"/><rect x="34" y="2" width="17" height="7" rx="2" fill="#1c1c1c"/><rect x="52" y="4" width="1.5" height="3" fill="#1c1c1c"/></svg>
    </header>
    <div class="brand-mark" style="top:225px"><span class="brand-dot"></span><span class="brand-name">NESTVPN</span></div>
    <p class="loading">Loading...</p>
    <svg class="spinner" width="28" height="28" viewBox="0 0 28 28" fill="#f4584a"><circle cx="14" cy="3" r="2.6"/><circle cx="21.8" cy="6.2" r="2.3"/><circle cx="25" cy="14" r="2"/><circle cx="21.8" cy="21.8" r="1.8"/><circle cx="14" cy="25" r="1.6"/><circle cx="6.2" cy="21.8" r="1.4"/><circle cx="3" cy="14" r="1.2"/><circle cx="6.2" cy="6.2" r="1"/></svg>
    <span class="home-bar" style="bottom:6px"></span>
  </section>

  <!-- Login -->
  <section class="screen" style="left:601px;top:78px">
    <header class="status"><span class="time">9:41</span>
      <svg class="icons" width="54" height="10" viewBox="0 0 54 10"><rect x="0" y="6" width="2" height="4" fill="#1c1c1c"/><rect x="3" y="4" width="2" height="6" fill="#1c1c1c"/><rect x="6" y="2" width="2" height="8" fill="#1c1c1c"/><rect x="9" y="0" width="2" height="10" fill="#1c1c1c"/><path d="M16 4a8 8 0 0 1 11 0M18 6a5 5 0 0 1 7 0" stroke="#1c1c1c" stroke-width="1.6" fill="none"/><circle cx="21.5" cy="8.5" r="1.3" fill="#1c1c1c"/><rect x="34" y="2" width="17" height="7" rx="2" fill="#1c1c1c"/><rect x="52" y="4" width="1.5" height="3" fill="#1c1c1c"/></svg>
    </header>
    <div class="brand-mark" style="top:145px"><span class="brand-dot" style="width:88px;height:88px"></span><span class="brand-name" style="margin-top:22px">NESTVPN</span></div>
    <span class="label" style="left:46px;top:312px">User ID</span>
    <div class="field" style="left:45px;top:334px"><span>email@example.com<span class="caret"></span></span><span class="clear"></span></div>
    <span class="label" style="left:46px;top:373px">Password</span>
    <div class="field" style="left:45px;top:394px"></div>
    <span class="small-note" style="left:48px;top:431px">Forgot Password?</span>
    <div class="pill-btn" style="left:45px;top:467px;width:202px;height:40px;line-height:40px;font-size:16px">Login</div>
    <p class="signup">Don't have an account yet? <b>Sign up here.</b></p>
    <span class="home-bar"></span>
  </section>

  <!-- Home -->
  <section class="screen" style="left:1143px;top:76px;height:651px">
    <header class="status" style="border:none"><span class="time">9:41</span>
      <svg class="icons" width="54" height="10" viewBox="0 0 54 10"><rect x="0" y="6" width="2" height="4" fill="#1c1c1c"/><rect x="3" y="4" width="2" height="6" fill="#1c1c1c"/><rect x="6" y="2" width="2" height="8" fill="#1c1c1c"/><rect x="9" y="0" width="2" height="10" fill="#1c1c1c"/><path d="M16 4a8 8 0 0 1 11 0M18 6a5 5 0 0 1 7 0" stroke="#1c1c1c" stroke-width="1.6" fill="none"/><circle cx="21.5" cy="8.5" r="1.3" fill="#1c1c1c"/><rect x="34" y="2" width="17" height="7" rx="2" fill="#1c1c1c"/><rect x="52" y="4" width="1.5" height="3" fill="#1c1c1c"/></svg>
    </header>
    <nav class="topnav"><span class="hamburger"></span><span class="nav-title">NESTVPN</span><span class="ping"><i></i>Ping Test</span></nav>
    <div class="status-band">Not Connected</div>
    <div class="quick">Quick Connect</div>
    <span class="section" style="top:160px">Favourites</span>
    <div class="card country" style="top:184px"><span class="flag de" role="img" aria-label="Germany flag"></span><span class="grow">Germany</span><span class="chev"></span></div>
    <span class="section" style="top:239px">Speciality Servers</span>
    <div class="card" style="top:263px"><span class="grow">Streaming Servers</span><span class="chev"></span></div>
    <div class="card" style="top:310px"><span class="grow">P2P Servers</span><span class="chev"></span></div>
    <div class="card" style="top:357px"><span class="grow">Onion over VPN</span><span class="chev"></span></div>
    <span class="section" style="top:410px">Country</span>
    <div class="card country" style="top:434px"><span class="flag us" role="img" aria-label="USA flag"></span><span class="grow">USA</span><span class="star">★</span><span class="chev"></span></div>
    <div class="card country" style="top:481px"><span class="flag uk" role="img" aria-label="UK flag"></span><span class="grow">UK</span><span class="star">★</span><span class="chev"></span></div>
    <div class="card country" style="top:528px"><span class="flag ca" role="img" aria-label="Canada flag"></span><span class="grow">Canada</span><span class="star">★</span><span class="chev"></span></div>
    <div class="card country" style="top:575px"><span class="flag in" role="img" aria-label="India flag"></span><span class="grow">India</span><span class="star gold">★</span><span class="chev"></span></div>
    <span class="home-bar"></span>
  </section>

  <!-- Side menu -->
  <section class="screen" style="left:67px;top:803px;width:301px;height:650px">
    <div class="menu-head"><span class="time">9:41</span><div class="menu-logo"><span></span><b>NESTVPN</b></div></div>
    <div class="menu-shade">
      <svg class="icons" width="54" height="10" viewBox="0 0 54 10"><rect x="0" y="6" width="2" height="4" fill="#1c1c1c"/><rect x="3" y="4" width="2" height="6" fill="#1c1c1c"/><rect x="6" y="2" width="2" height="8" fill="#1c1c1c"/><rect x="9" y="0" width="2" height="10" fill="#1c1c1c"/><path d="M16 4a8 8 0 0 1 11 0M18 6a5 5 0 0 1 7 0" stroke="#1c1c1c" stroke-width="1.6" fill="none"/><circle cx="21.5" cy="8.5" r="1.3" fill="#1c1c1c"/><rect x="34" y="2" width="17" height="7" rx="2" fill="#1c1c1c"/><rect x="52" y="4" width="1.5" height="3" fill="#1c1c1c"/></svg>
      <span class="ping"><i></i>Ping Test</span>
      <span class="shade-band"></span>
      <span class="shade-blue"></span>
      <div class="stub" style="top:184px"><span class="chev"></span></div>
      <div class="stub" style="top:263px"><span class="chev"></span></div>
      <div class="stub" style="top:310px"><span class="chev"></span></div>
      <div class="stub" style="top:357px"><span class="chev"></span></div>
      <div class="stub" style="top:433px"><span class="star">★</span><span class="chev"></span></div>
      <div class="stub" style="top:481px"><span class="star">★</span><span class="chev"></span></div>
      <div class="stub" style="top:528px"><span class="star">★</span><span class="chev"></span></div>
      <div class="stub" style="top:575px"><span class="star gold">★</span><span class="chev"></span></div>
    </div>
    <div class="menu-item active" style="top:163px">Home</div>
    <div class="menu-item" style="top:205px">Settings</div>
    <div class="menu-item" style="top:244px">Support Center</div>
    <div class="menu-item" style="top:283px">Logout</div>
    <span class="home-bar" style="left:95px"></span>
  </section>

  <!-- Protocols -->
  <section class="screen" style="left:421px;top:803px;height:650px">
    <header class="status"><span class="time">9:41</span>
      <svg class="icons" width="54" height="10" viewBox="0 0 54 10"><rect x="0" y="6" width="2" height="4" fill="#1c1c1c"/><rect x="3" y="4" width="2" height="6" fill="#1c1c1c"/><rect x="6" y="2" width="2" height="8" fill="#1c1c1c"/><rect x="9" y="0" width="2" height="10" fill="#1c1c1c"/><path d="M16 4a8 8 0 0 1 11 0M18 6a5 5 0 0 1 7 0" stroke="#1c1c1c" stroke-width="1.6" fill="none"/><circle cx="21.5" cy="8.5" r="1.3" fill="#1c1c1c"/><rect x="34" y="2" width="17" height="7" rx="2" fill="#1c1c1c"/><rect x="52" y="4" width="1.5" height="3" fill="#1c1c1c"/></svg>
    </header>
    <nav class="topnav"><span class="back">‹ Settings</span><span class="page-title" style="left:123px">Protocols</span></nav>
    <h2 class="group-title">Protocol Selection</h2>
    <div class="list">
      <div class="row"><h3>Automatic</h3><p>Let NestVPN chose the best Protocol</p>
        <svg class="tick" width="16" height="12" viewBox="0 0 16 12"><path d="M1 6l5 5 9-10" stroke="#f4584a" stroke-width="2" fill="none"/></svg></div>
      <div class="row"><h3>IPSec</h3><p>The most secure Protocol</p></div>
      <div class="row"><h3>IKEv2</h3><p>The most stable Protocol</p></div>
    </div>
    <span class="home-bar" style="left:94px"></span>
  </section>

  <!-- Settings -->
  <section class="screen" style="left:789px;top:803px;height:650px">
    <header class="status"><span class="time">9:41</span>
      <svg class="icons" width="54" height="10" viewBox="0 0 54 10"><rect x="0" y="6" width="2" height="4" fill="#1c1c1c"/><rect x="3" y="4" width="2" height="6" fill="#1c1c1c"/><rect x="6" y="2" width="2" height="8" fill="#1c1c1c"/><rect x="9" y="0" width="2" height="10" fill="#1c1c1c"/><path d="M16 4a8 8 0 0 1 11 0M18 6a5 5 0 0 1 7 0" stroke="#1c1c1c" stroke-width="1.6" fill="none"/><circle cx="21.5" cy="8.5" r="1.3" fill="#1c1c1c"/><rect x="34" y="2" width="17" height="7" rx="2" fill="#1c1c1c"/><rect x="52" y="4" width="1.5" height="3" fill="#1c1c1c"/></svg>
    </header>
    <nav class="topnav"><span class="back">‹ Home</span><span class="page-title" style="left:123px">Settings</span></nav>
    <h2 class="group-title" style="left:28px">App Settings</h2>
    <div class="list">
      <div class="row switch"><h3>Killswitch</h3><p style="width:195px">Cuts Internet connectivity when your VPN connection gets lost</p><span class="toggle"></span></div>
      <div class="row link"><svg width="16" height="18" viewBox="0 0 16 18"><path d="M8 1l7 3v5c0 4-3 7-7 8-4-1-7-4-7-8V4z" fill="#1c1c1c"/><path d="M4.5 9l2.5 2.5 4.5-5" stroke="#fff" stroke-width="1.6" fill="none"/></svg><span style="flex:1">Protocols</span><span class="chev" style="margin-right:8px"></span></div>
      <div class="row link danger"><svg width="18" height="18" viewBox="0 0 18 18"><rect x="1" y="1" width="10" height="16" rx="1" fill="#f4584a"/><path d="M9 9h8M14 6l3 3-3 3" stroke="#f4584a" stroke-width="1.8" fill="none"/><circle cx="8" cy="9" r="1" fill="#fff"/></svg>Logout</div>
    </div>
    <span class="footer-links" style="top:524px">Terms of Service</span>
    <span class="footer-links" style="top:548px">Privacy Policy</span>
    <span class="footer-links" style="top:584px;color:#555;font-size:13px">App Version v1.0a.</span>
    <span class="home-bar" style="left:94px"></span>
  </section>

  <!-- Forgot password -->
  <section class="screen" style="left:1143px;top:803px;height:650px">
    <header class="status"><span class="time">9:41</span>
      <svg class="icons" width="54" height="10" viewBox="0 0 54 10"><rect x="0" y="6" width="2" height="4" fill="#1c1c1c"/><rect x="3" y="4" width="2" height="6" fill="#1c1c1c"/><rect x="6" y="2" width="2" height="8" fill="#1c1c1c"/><rect x="9" y="0" width="2" height="10" fill="#1c1c1c"/><path d="M16 4a8 8 0 0 1 11 0M18 6a5 5 0 0 1 7 0" stroke="#1c1c1c" stroke-width="1.6" fill="none"/><circle cx="21.5" cy="8.5" r="1.3" fill="#1c1c1c"/><rect x="34" y="2" width="17" height="7" rx="2" fill="#1c1c1c"/><rect x="52" y="4" width="1.5" height="3" fill="#1c1c1c"/></svg>
    </header>
    <nav class="topnav"><span class="back">‹ Login</span><span class="page-title" style="left:89px">Forgot Password</span></nav>
    <h2 class="forgot-head" style="font-weight:400">Did you forget your Password?</h2>
    <p class="forgot-copy">If you have forgotten your password, enter the email address associated with your account into the box below and we will send you instructions on how to reset your password to your email account</p>
    <span class="label" style="left:29px;top:195px">Email Address</span>
    <div class="field" style="left:28px;top:217px"><span>email@example.com<span class="caret"></span></span><span class="clear"></span></div>
    <div class="pill-btn submit">Submit Password Reset Request</div>
    <span class="home-bar" style="left:94px"></span>
  </section>

</div>
</body>
</html>
```